Northfield Energy Product Distribution Brochure

We are looking to have our current brochure for our customers completely redesigned...the idea is to present the relevant information in an attractive way . Our website is northfieldenergy-example.com where you can find more information about us. We have included a file with a rough idea of the page order and what each should include but feel free to adapt based on design. The example provided is only for context and doesnt have to be maintained. We will be using the brochure both digitally and in print form. As long as it reads easily and is eye catching, the design can be horizontal or vertical.Final deliverable should be indesign file.

"Our Brands" page: should be limited to one page (space being enough) where it has the header for each one (for example diesel generators) space for one or two lines of text and then the corresponding logos for each of the five categories
Updates

For those asking: the "our brands" page should be a single page layout where there is a header with the corresponding section and space for maybe one line of text followed by the two logos for that category. Each of the product pages should be similar in fashion to the one in the document attached: a photo of the product with some white space and space for the text to be included. We will be posting additional examples today

Target Market(s)

We want to present it to customers both digitally and in print so they can see our products

Industry/Entity Type

Power Generation

Font styles to use
Serif

Requirements
Must have
• Eye catching and able to present the information in a presentable fashion. Rest is up to you.
Nice to have
• Should incorporate the colors of our logo but can also add other depending on design

```html
<!DOCTYPE html>
<html lang="en">
<head>
<meta charset="utf-8">
<title>Northfield Energy – Distributor Program Guide</title>
<link href="https://fonts.googleapis.com/css2?family=Montserrat:wght@400;600;700&family=Open+Sans:wght@400;600&display=swap" rel="stylesheet">
<style>
:root{
  --stage:#e4e4e4;
  --paper:#ffffff;
  --paper-grey:#ececec;
  --panel:#f1f1f1;
  --ink:#2b2b2b;
  --charcoal:#3a3a3a;
  --black:#232323;
  --gold:#e3a514;
  --yellow:#f5c21b;
  --muted:#6b6b6b;
}
*{box-sizing:border-box;margin:0;padding:0}
html,body{width:1200px;height:900px;overflow:hidden;background:var(--stage);font-family:"Open Sans",Arial,sans-serif;color:var(--ink)}
.canvas{position:relative;width:1200px;height:900px}
.spread{position:absolute;display:flex;box-shadow:0 8px 24px rgba(0,0,0,.15)}
.spread--cover{left:180px;top:30px;width:840px;height:380px}
.spread--inner{left:100px;top:445px;width:1000px;height:420px}
.page{position:relative;flex:1;overflow:hidden;background:var(--paper)}
.page svg.bg{position:absolute;inset:0;width:100%;height:100%}
.heading{font-family:"Montserrat",Arial,sans-serif}

/* back cover */
.back-cover{background:var(--paper-grey)}
.back-cover .band{position:absolute;left:0;right:0;top:200px;height:120px;background:var(--black)}
.back-cover .frame{position:absolute;left:60px;top:50px;width:300px;height:280px;border:2px solid var(--gold)}
.brand{position:absolute;display:flex;align-items:center;gap:8px;font-family:"Montserrat",Arial,sans-serif;font-weight:600;color:var(--charcoal)}
.brand .mark{width:22px;height:22px;background:var(--gold)}
.brand--back{left:110px;top:110px;font-size:20px}
.tagline{position:absolute;font-family:"Montserrat",Arial,sans-serif;font-size:7px;letter-spacing:3px;color:var(--muted)}
.tagline--back{left:140px;top:142px}
.contact{position:absolute;left:60px;width:300px;top:215px;text-align:center;color:var(--gold);font-family:"Montserrat",Arial,sans-serif}
.contact h3{font-size:14px;font-weight:600;margin-bottom:18px}
.contact p{font-size:10px;line-height:1.9}

/* front cover */
.cover-photo{position:absolute;left:150px;top:0;width:270px;height:165px;background:linear-gradient(120deg,#d9d9d9,#f4f4f4 45%,#9c9c9c)}
.cover-title{position:absolute;left:200px;top:180px;color:var(--yellow);font-family:"Montserrat",Arial,sans-serif;font-weight:700;font-size:22px;line-height:1.05}
.cover-sub{position:absolute;left:200px;top:258px;font-size:8px;color:#cfcfcf}
.brand--front{left:30px;top:250px;font-size:12px;color:#d6d6d6}
.brand--front .mark{width:14px;height:14px}
.tagline--front{left:52px;top:268px;font-size:5px;color:#bdbdbd}
.cover-badges{position:absolute;left:30px;top:305px;display:flex;gap:22px}
.badge{display:flex;flex-direction:column;align-items:center;gap:3px;font-size:6px;color:var(--muted);text-transform:uppercase;text-align:center;width:46px}
.badge svg{width:20px;height:20px}

/* contents */
.contents-title{position:absolute;left:20px;top:0;width:220px;height:75px;background:var(--gold);padding:14px 0 0 28px;color:var(--ink)}
.contents-title span{display:block;font-size:20px;font-weight:400;line-height:1.1}
.contents-title strong{display:block;font-size:26px;font-weight:700;line-height:1.1}
.contents-panel{position:absolute;left:20px;top:95px;width:445px;height:240px;background:var(--panel);padding:10px 70px 0 30px}
.toc-row{display:flex;justify-content:space-between;align-items:center;border-bottom:1.5px solid #555;height:53px;font-size:6.5px;font-weight:600;line-height:1.6}
.toc-row .num{font-family:"Montserrat",Arial,sans-serif;font-size:16px;font-weight:400}
.contents-bar{position:absolute;right:0;bottom:25px;width:300px;height:20px;background:#4a4444}

/* who we are */
.about-title{position:absolute;left:30px;top:28px;width:275px;font-size:14px;font-weight:700;border-bottom:1.5px solid #888;padding-bottom:6px}
.about-body{position:absolute;left:30px;top:68px;width:280px;font-size:6.3px;line-height:1.6;color:#444}
.about-body p{margin-bottom:9px}
.about-body em{font-style:normal;color:var(--gold)}
.about-photo{position:absolute;right:0;top:0;width:160px;height:390px;background:linear-gradient(180deg,#fafafa 0%,#f0f0f0 15%,#3c3c3c 35%,#2a2a2a 80%,#8d8d8d 100%)}
.about-bar{position:absolute;left:0;bottom:20px;width:300px;height:22px;background:var(--yellow)}
.page-num{position:absolute;right:8px;bottom:22px;font-family:"Montserrat",Arial,sans-serif;font-size:12px;font-weight:600}
</style>
</head>
<body>
<main class="canvas">

  <section class="spread spread--cover">
    <article class="page back-cover">
      <div class="band"></div>
      <div class="frame"></div>
      <div class="brand brand--back"><span class="mark"></span>Northfield Energy</div>
      <div class="tagline tagline--back">THE GENERATOR COMPANY</div>
      <div class="contact">
        <h3>Contact Us</h3>
        <p>1250 Harbor Ave, Tampa, FL 33602<br>(555) 014-2280</p>
      </div>
    </article>

    <article class="page front-cover">
      <svg class="bg" viewBox="0 0 420 380" preserveAspectRatio="none" aria-hidden="true">
        <rect width="420" height="380" fill="#f2f2f2"/>
        <path d="M0 60 Q60 20 130 0 L160 0 Q70 40 20 140 Z" fill="#e3a514"/>
        <path d="M20 140 Q60 70 160 0 L175 0 Q90 60 45 170 Z" fill="#3a3a3a"/>
        <polygon points="0,170 420,130 420,300 0,300" fill="#3a3a3a"/>
        <path d="M300 300 Q380 260 420 200 L420 300 Z" fill="#f5c21b"/>
        <rect x="0" y="300" width="420" height="80" fill="#ffffff"/>
      </svg>
      <div class="cover-photo" role="img" aria-label="Photo of a trailer-mounted diesel generator set"></div>
      <div class="brand brand--front"><span class="mark"></span>Northfield Energy</div>
      <div class="tagline tagline--front">THE GENERATOR COMPANY</div>
      <h1 class="cover-title">DISTRIBUTOR<br>PROGRAM<br>GUIDE</h1>
      <p class="cover-sub">Diesel Generators | Alternators | Parts</p>
      <div class="cover-badges">
        <div class="badge">
          <svg viewBox="0 0 20 20" fill="none" stroke="#6b6b6b" stroke-width="1.2"><circle cx="10" cy="6" r="3.5"/><path d="M3 18c0-4 3-6 7-6s7 2 7 6"/></svg>
          Team of experts
        </div>
        <div class="badge">
          <svg viewBox="0 0 20 20" fill="none" stroke="#6b6b6b" stroke-width="1.2"><circle cx="10" cy="10" r="8"/><path d="M10 5v5l3 2"/></svg>
          Same day urgency
        </div>
        <div class="badge">
          <svg viewBox="0 0 20 20" fill="none" stroke="#6b6b6b" stroke-width="1.2"><circle cx="10" cy="10" r="8"/><path d="M6 10l3 3 5-6"/></svg>
          100% original
        </div>
      </div>
    </article>
  </section>

  <section class="spread spread--inner">
    <article class="page contents">
      <div class="contents-title heading"><span>PAGE OF</span><strong>CONTENT</strong></div>
      <div class="contents-panel">
        <div class="toc-row"><span>Lorem ipsum dolor sit amet, consectetur<br>adipiscing elit, sed do eiusmod tempor incididunt</span><span class="num">01</span></div>
        <div class="toc-row"><span>Lorem ipsum dolor sit amet, consectetur<br>adipiscing elit, sed do eiusmod tempor incididunt</span><span class="num">02</span></div>
        <div class="toc-row"><span>Lorem ipsum dolor sit amet, consectetur<br>adipiscing elit, sed do eiusmod tempor incididunt</span><span class="num">03</span></div>
        <div class="toc-row"><span>Lorem ipsum dolor sit amet, consectetur<br>adipiscing elit, sed do eiusmod tempor incididunt</span><span class="num">04</span></div>
      </div>
      <div class="contents-bar"></div>
    </article>

    <article class="page about">
      <h2 class="about-title heading">WHO WE ARE</h2>
      <div class="about-body">
        <p>With over 20 years industry experience delivering <em>100,000+</em> power generation solutions across the Americas, Northfield Energy is pleased to introduce the Northfield line of heavy duty <em>industrial diesel generators from 20 to 500kW</em>. Holding to our roots our philosophy of work will continue: extensive stock, short lead times, specialized customizable products and pre-configured units to meet your needs. Focusing on six market segments – <em>Industrial, Mobile, Agricultural, Commercial Mobile and Compact Mobile</em> – allows us to offer a wholistic line of products that satisfies most markets and clients.</p>
        <p>We understand the need for an <em>innovative, versatile, and reliable partner</em> in today's competitive market, and with over two decades of success in power generation and distribution of the highest quality brands, we are prepared to supply customized solutions for even the most complex and urgent requirements. Providing our distributors with <em>sales and technical training, online platform, custom referrals, marketing material</em> and strong products allows them to compete with big brands. We ensure our distributors have what they need to close the sale and keep clients.</p>
        <p>Additional to our OEM capabilities, Northfield Energy is also <em>Master Distributor for several leading engine, alternator, control and switchgear makers</em>, making us a single source for <em>diesel generators, AC alternators, alternator parts, generator controllers and power transfer switches</em>. Our central location is minutes away from <em>regional seaports, the international airport and many freight forwarders</em>, enabling us to serve users around the Americas.</p>
      </div>
      <div class="about-photo" role="img" aria-label="Photo of an engineer in a yellow hard hat writing on a clipboard"></div>
      <div class="about-bar"></div>
      <div class="page-num">03</div>
    </article>
  </section>

</main>
</body>
</html>
```